Prepare a modern, professional business card for Bramford Ledger Services (BLS) Our company is in the banking, compliance and finance industry. We provide kiosks, software integration, and compliance guidelines so that banks can "bank" Marijuana Dispensaries with TrevMon, Office of Halvern Affairs and NTRB approval.

Target Market(s)

Banks

Industry/Entity Type

Business

Contact Information for Business Card

Owen R Pelley
Bramford Ledger Services
Vice President
742 Quarry Ridge Road
Suite 310
Las Vegas, NV 89135
owen@bramfordls.net
702-555-0147

Font styles to use
Sans Serif

Requirements
Nice to have
• I like the clean simple appearance of Quillon computers. Perhaps the three LETTERS of BLS can be the LOGO on the Card and the Company name could be incorporated in the contact information. Like colors of white, black and gray

```html
<!DOCTYPE html>
<html lang="en">
<head>
<meta charset="UTF-8">
<title>Bramford Ledger Services – Business Card</title>
<link href="https://fonts.googleapis.com/css2?family=Jost:wght@300&family=Source+Sans+3:wght@400;600&display=swap" rel="stylesheet">
<style>
  :root {
    --page-bg: #cccccc;
    --card-bg: #999999;
    --ink-dark: #2e2e2e;
    --ink-light: #f4f4f4;
    --divider: #ffffff;
    --icon-bg: #333333;
  }
  * { margin: 0; padding: 0; box-sizing: border-box; }
  html, body {
    width: 1200px; height: 1200px; overflow: hidden;
    background: var(--page-bg);
  }
  .business-card {
    position: absolute;
    left: 233px; top: 367px;
    width: 715px; height: 418px;
    background: var(--card-bg);
  }
  .holder-name, .holder-title {
    position: absolute;
    font-family: "Jost", sans-serif;
    font-weight: 300;
    color: var(--ink-dark);
    white-space: nowrap;
  }
  .holder-name { left: 64px; top: 48px; font-size: 39px; letter-spacing: 0.5px; }
  .title-divider {
    position: absolute; left: 408px; top: 53px;
    width: 3px; height: 44px; background: var(--divider);
  }
  .holder-title { left: 453px; top: 50px; font-size: 35px; color: #3a3a3a; }
  .brand-mark {
    position: absolute; left: 0; width: 100%; top: 168px;
    text-align: center;
    font-family: "Source Sans 3", sans-serif;
    font-weight: 600; font-size: 82px; line-height: 1;
    color: var(--ink-dark); letter-spacing: 2px;
  }
  .company-name {
    position: absolute; left: 0; width: 100%; top: 272px;
    text-align: center;
    font-family: "Source Sans 3", sans-serif;
    font-weight: 600; font-size: 23px; letter-spacing: 0.6px;
    color: var(--ink-dark);
  }
  .contact-row {
    position: absolute; left: 48px; top: 362px;
    display: flex; align-items: center; gap: 8px;
    font-family: "Source Sans 3", sans-serif;
    font-weight: 600; font-size: 13.5px;
    color: var(--ink-light); white-space: nowrap;
  }
  .contact-icon { width: 16px; height: 16px; flex: none; }
  .contact-item { margin-right: 10px; }
  .contact-item:last-child { margin-right: 0; }
</style>
</head>
<body>
  <div class="business-card">
    <div class="holder-name">OWEN R PELLEY</div>
    <div class="title-divider"></div>
    <div class="holder-title">Vice President</div>

    <div class="brand-mark">BLS</div>
    <div class="company-name">BRAMFORD LEDGER SERVICES</div>

    <div class="contact-row">
      <svg class="contact-icon" viewBox="0 0 16 16" aria-hidden="true">
        <circle cx="8" cy="8" r="8" fill="var(--icon-bg)"/>
        <rect x="4" y="5" width="8" height="6" fill="none" stroke="#fff" stroke-width="1"/>
        <path d="M4 5 L8 8.5 L12 5" fill="none" stroke="#fff" stroke-width="1"/>
      </svg>
      <span class="contact-item">owen@bramfordls.net</span>
      <svg class="contact-icon" viewBox="0 0 16 16" aria-hidden="true">
        <circle cx="8" cy="8" r="8" fill="var(--icon-bg)"/>
        <path d="M5 11.5 C5 7.5 7.5 5 11 4.5 L11 6.3 C8.6 6.8 7 8.5 6.8 11.5 Z" fill="#fff"/>
      </svg>
      <span class="contact-item">702-555-0147</span>
      <svg class="contact-icon" viewBox="0 0 16 16" aria-hidden="true">
        <circle cx="8" cy="8" r="8" fill="var(--icon-bg)"/>
        <path d="M8 3.8 L12.5 8 L11.2 8 L11.2 11.8 L9 11.8 L9 9.3 L7 9.3 L7 11.8 L4.8 11.8 L4.8 8 L3.5 8 Z" fill="#fff"/>
      </svg>
      <span class="contact-item">742 Quarry Ridge Road Suite, 310 Las Vegas, NV 89135</span>
    </div>
  </div>
</body>
</html>
```